Fresh looking flyer for Vantrel Academy Of Computing

We need a flyer design for our IT school that will be distributed to potential students during our recruitment campaign. We want to feature the following aspects of the school:

-Study IT in a nordic/european way close to your home (design should feel Scandinavian)
-Featuring the dean of the school (photo attached)
-Match the theme of logo (logo attached)
-A potential layout attached as a mockup

CONTENT
* Main Message " LEARN EUROPEAN PROGRAMMING COURSES IN BEKASI"
* Sub Message " 3 MONTH MODULES FROM BEGINNER TO ADVANCED"
* Campaign " ATTEND FREE CLASS & GET 10% OFF COURSE, SIGN UP BETWEEN 7-18MARCH. vantrel.example/free
* Extra info: " GRADUATE AND GET HIRED TO EARN 120 MILLION IDR/YEAR"

End result should be in Adobe Illustrator format.

Target Market(s)

18-30 year old Indonesians interested in IT

Industry/Entity Type

Education

Font styles to use
Sans Serif

Colors
85cae6

Requirements
Must have
• -Photo of the manager
• -Messages as in the project description
• -School logo
• -Nordic look and feel

```html
<!DOCTYPE html>
<html lang="en">
<head>
<meta charset="utf-8">
<title>Vantrel Academy Of Computing – Flyer</title>
<link rel="stylesheet" href="https://fonts.googleapis.com/css2?family=Montserrat:wght@300;400;600;700&family=Fira+Sans:wght@700&display=swap">
<style>
  :root {
    --night: #0b0b0c;
    --cream: #f4f0d8;
    --sky-blue: #7fa6dc;
    --sky-light: #85cae6;
    --paper-white: #ffffff;
    --navy: #24438a;
    --note: #f4f1e8;
    --note-red: #b1242c;
  }
  * { margin: 0; padding: 0; box-sizing: border-box; }
  html, body { width: 1200px; height: 815px; overflow: hidden; background: #ffffff; }
  .flyer {
    position: relative;
    width: 1200px;
    height: 815px;
    overflow: hidden;
    font-family: "Montserrat", Arial, sans-serif;
    background: var(--paper-white);
  }
  .backdrop { position: absolute; inset: 0; }
  .dean-portrait {
    position: absolute;
    left: 690px;
    top: 36px;
    width: 510px;
    height: 779px;
    border-radius: 230px 230px 0 0;
    background: linear-gradient(180deg, #cfc3b4 0%, #dcd6cf 45%, #eceef1 62%, #f3f4f6 100%);
  }
  .headline {
    position: absolute;
    left: 80px;
    top: 66px;
    color: var(--cream);
    font-weight: 600;
    text-transform: uppercase;
    line-height: 1;
  }
  .headline-top { display: block; font-size: 37px; letter-spacing: 0.4px; }
  .headline-main { display: block; font-size: 66px; font-weight: 700; margin-top: 7px; letter-spacing: 4px; }
  .headline-main .joiner { font-size: 30px; font-weight: 600; letter-spacing: 1px; margin: 0 6px 0 2px; }
  .module {
    position: absolute;
    left: 82px;
    top: 201px;
    color: var(--sky-blue);
    text-transform: uppercase;
    line-height: 1.15;
  }
  .module-title { display: block; font-size: 28px; font-weight: 700; letter-spacing: 10px; }
  .module-range { display: block; font-size: 25px; font-weight: 300; margin-top: 2px; letter-spacing: 0.2px; }
  .campaign {
    position: absolute;
    left: 82px;
    top: 281px;
    color: #ffffff;
    font-size: 17px;
    font-weight: 300;
    line-height: 26.5px;
    text-transform: uppercase;
  }
  .campaign strong { font-weight: 700; }
  .campaign .url { text-transform: none; font-weight: 400; }
  .brand {
    position: absolute;
    left: 76px;
    top: 750px;
    display: flex;
    align-items: center;
    gap: 12px;
    color: var(--navy);
    font-size: 23px;
    font-weight: 400;
    text-transform: uppercase;
    letter-spacing: 0.3px;
  }
  .brand-dot { width: 22px; height: 22px; border-radius: 50%; background: var(--navy); }
  .hire-note {
    position: absolute;
    left: 946px;
    top: 552px;
    width: 186px;
    height: 202px;
    background: var(--note);
    display: flex;
    flex-direction: column;
    justify-content: center;
    align-items: center;
    text-align: center;
    font-family: "Fira Sans", Arial, sans-serif;
    font-weight: 700;
    color: var(--note-red);
    font-size: 19px;
    line-height: 25px;
    text-transform: uppercase;
  }
  .hire-note .small { text-transform: none; }
</style>
</head>
<body>
<main class="flyer">
  <svg class="backdrop" width="1200" height="815" viewBox="0 0 1200 815">
    <defs>
      <linearGradient id="skyFill" x1="0" y1="0" x2="0" y2="1">
        <stop offset="0" stop-color="#5c93cf"/>
        <stop offset="1" stop-color="#b9d6e6"/>
      </linearGradient>
    </defs>
    <rect role="img" aria-label="Window view over a Nordic fell landscape under a blue sky" x="0" y="180" width="1200" height="600" fill="url(#skyFill)"/>
    <path class="night-band" d="M0 0 H1200 V198 C900 200 650 260 430 340 C250 405 110 470 0 516 Z" fill="var(--night)"/>
    <path class="white-wave" d="M0 624 C200 690 450 725 700 735 L1200 735 V815 H0 Z" fill="var(--paper-white)"/>
  </svg>

  <div class="dean-portrait" role="img" aria-label="Photo of the school's dean in a white shirt, holding a clipboard"></div>

  <h1 class="headline">
    <span class="headline-top">Learn European Programming</span>
    <span class="headline-main">Courses<span class="joiner">in</span>Bekasi</span>
  </h1>

  <p class="module">
    <span class="module-title">3 Month Module</span>
    <span class="module-range">From Beginner to Advanced</span>
  </p>

  <p class="campaign">
    Attend free class<br>
    &amp; <strong>Get 10% off course</strong>,<br>
    Sign up between<br>
    7-18 March.<br>
    <span class="url">vantrel.example/free</span>
  </p>

  <p class="hire-note">Graduate<br>and get hire<br><span class="small">to</span>Earn<br>120 Million<br>IDR/Year</p>

  <div class="brand">
    <span class="brand-dot"></span>
    <span class="brand-name">Vantrel Academy Of Computing</span>
  </div>
</main>
</body>
</html>
```